Brontaro Web Site

Redesigned web site for Brontaro Ltd (www.brontaro-example.co.uk). This is to feature new logo (attached). Brontaro Ltd is a company which specialises in Geographic Information Systems and Geographic data - we call ourselves GIS Data Specialists. We are looking for something which conveys our professionalism and our experience. There will be more pages than on the current Brontaro website. There will be: Home, Data Migration, Data Cleansing & Validation, Data Analysis, Data Maintenance, Data Quality and an About Us page. All these should be accessible from each page on the website.
Updates
I didn't really think to say that the content of the web site is going to change from the current one we have. There will be more pages than on the current one. They will be: Home, Data Migration, Data Cleansing & Validation, Data Analysis, Data Maintenance, Data Quality and an About Us page. All these should be accessible from each page on the website. I didn't really think through the fact that the number of pages / areas to access can influence the layout of the site, sorry.
Target Market(s)
Utility Companies (e.g. telecommunications providers, energy companies), local government.
Industry/Entity Type
It Company
Look and feel

```html
<!DOCTYPE html>
<html lang="en">
<head>
<meta charset="utf-8">
<title>Brontaro – GIS Data Specialists</title>
<link rel="stylesheet" href="https://fonts.googleapis.com/css2?family=Ubuntu:wght@400;500;700&family=Arimo:wght@400;700&family=Cinzel:wght@500&display=swap">
<style>
:root{
  --sky:#9dd8dc;
  --teal:#2aa6a8;
  --teal-soft:#7cc8cc;
  --grey-dark:#555;
  --grey:#666;
  --grey-logo:#888;
  --red:#c1272d;
  --green-dark:#1f7a55;
  --green:#2f8f66;
  --white:#fff;
}
*{margin:0;padding:0;box-sizing:border-box}
html,body{width:1200px;height:981px;overflow:hidden}
body{position:relative;background:var(--white);font-family:"Ubuntu",sans-serif;color:var(--grey)}
.band-top{position:absolute;left:0;top:0;width:1200px;height:190px;background:var(--sky)}
.band-foot{position:absolute;left:0;top:907px;width:1200px;height:74px;background:var(--sky)}
.page{position:absolute;left:100px;top:12px;width:1000px;height:895px;background:var(--white)}

.brand{position:absolute;left:35px;top:32px;display:flex;align-items:center;gap:14px}
.brand-mark{width:56px;height:56px;border-radius:50%;background:var(--teal-soft)}
.brand-name{font-size:49px;font-weight:500;color:var(--grey-logo);line-height:1}
.brand-tag{font-size:20px;color:var(--grey-logo);margin-top:1px;line-height:1}

.util{position:absolute;right:33px;top:27px;font-size:12px;font-weight:500;color:var(--grey-logo);display:flex;gap:14px}
.util span.sep{color:#aaa}

.care{position:absolute;left:650px;top:57px;width:318px;height:92px;background:var(--sky)}
.care-key{position:absolute;left:22px;top:-12px;width:106px;height:104px;border-radius:14px;background:linear-gradient(145deg,#fff,#d9d9d9);transform:rotate(12deg)}
.care-text{position:absolute;left:136px;top:5px;width:180px;text-align:center;font-weight:700;color:#111;font-size:16px;line-height:27px}
.care-phone{color:var(--red);font-size:21px}

.nav{position:absolute;left:0;top:178px;width:1000px;height:51px;border:1px dotted var(--teal-soft);border-top:none}
.nav ul{list-style:none;display:flex;position:absolute;left:17px;top:22px;font-family:"Arimo",sans-serif;font-size:10.5px;color:var(--teal);white-space:nowrap}
.nav li{display:flex;align-items:center}
.nav li+li::before{content:"";width:4px;height:4px;border-radius:50%;background:#999;margin:0 7px}
.search{position:absolute;left:811px;top:16px;width:140px;height:22px;border:1px solid #aaa;font-size:11px;color:#aaa;padding:4px 7px}
.search-go{position:absolute;left:960px;top:16px;width:24px;height:22px;border:1px solid #aaa;font-size:12px;color:#666;text-align:center;line-height:20px}

.hero{position:absolute;left:-1px;top:242px;width:1001px;height:197px;background:linear-gradient(90deg,var(--green-dark),var(--green) 60%,var(--green-dark))}
.hero-image{position:absolute;left:0;top:0;width:362px;height:197px;background:linear-gradient(90deg,#1c1c1c 0%,#2d2d2d 30%,#2b7a59 60%,#2f8f66)}
.hero-title{position:absolute;left:405px;top:43px;font-family:"Cinzel",serif;font-weight:500;font-size:18.5px;color:var(--white);letter-spacing:.3px}
.hero-copy{position:absolute;left:405px;top:78px;width:505px;font-size:10.5px;line-height:18px;color:var(--white)}

.side{position:absolute;left:18px;top:484px;list-style:none}
.side li{height:33px;display:flex;align-items:flex-start;font-size:13px;color:var(--grey)}
.side svg{margin-right:15px;margin-top:2px}
.side a{color:inherit;text-decoration:underline}
.side-rule{position:absolute;left:222px;top:490px;width:2px;height:220px;background:linear-gradient(#fff,#e4e4e4 40%,#e4e4e4 60%,#fff)}

.main{position:absolute;left:272px;top:486px;width:708px;font-size:12px;line-height:18px;color:var(--grey)}
.main h1{font-size:17.5px;font-weight:500;color:var(--red);margin-bottom:19px}
.main p{margin-bottom:18px}
.services{list-style:none;margin-left:36px;font-size:13px;line-height:22px;margin-top:-6px}
.services li{color:var(--red)}
.services a{color:var(--red);text-decoration:underline}

.copyright{position:absolute;left:102px;top:926px;font-size:12px;font-weight:500;color:var(--grey-dark)}
.social{position:absolute;left:908px;top:919px;display:flex;gap:4px}
.social span{display:block;height:25px;background:#3b5c9a}
</style>
</head>
<body>
<div class="band-top"></div>
<div class="band-foot"></div>

<div class="page">
  <header>
    <div class="brand">
      <div class="brand-mark"></div>
      <div>
        <div class="brand-name">Brontaro</div>
        <div class="brand-tag">GIS Data Specialists</div>
      </div>
    </div>
    <div class="util"><span>Login</span><span class="sep">|</span><span>Register</span><span class="sep">|</span><span>Contact</span></div>
    <div class="care">
      <div class="care-key" role="img" aria-label="Help key on a keyboard"></div>
      <div class="care-text">24/7 Customer Care<br>Call @<br><span class="care-phone">1800 5550192</span></div>
    </div>
  </header>

  <nav class="nav">
    <ul>
      <li>HOME</li><li>DATA MIGRATION</li><li>DATA CLEANSING &amp; VALIDATION</li><li>DATA ANALYSIS</li><li>DATA MAINTENANCE</li><li>DATA QUALITY</li><li>ABOUT US</li>
    </ul>
    <div class="search">Search Text Here..</div>
    <div class="search-go">go</div>
  </nav>

  <section class="hero">
    <div class="hero-image" role="img" aria-label="Businessman giving a thumbs up beside a rising chart chalked on a green board"></div>
    <h2 class="hero-title">SUCCESSFULL MARKETING STRATEGIES</h2>
    <p class="hero-copy">We provide a vast bank of knowledge and experience to offer an all encompassing service. This ensures that you, as a customer, reap the maximum benefits from your data and systems through utilising a combination of our skilled consultants, analysts and developers that will work with you and your requirements to help achieve your business objectives.</p>
  </section>

  <ul class="side">
    <li><svg width="8" height="14"><path d="M0 0L8 7L0 14Z" fill="#7cc8cc"/></svg><a>home</a></li>
    <li><svg width="8" height="14"><path d="M0 0L8 7L0 14Z" fill="#7cc8cc"/></svg><a>data migration</a></li>
    <li><svg width="8" height="14"><path d="M0 0L8 7L0 14Z" fill="#7cc8cc"/></svg><a>data cleansing &amp; validation</a></li>
    <li><svg width="8" height="14"><path d="M0 0L8 7L0 14Z" fill="#7cc8cc"/></svg><a>data analysis</a></li>
    <li><svg width="8" height="14"><path d="M0 0L8 7L0 14Z" fill="#7cc8cc"/></svg><a>data maintenance</a></li>
    <li><svg width="8" height="14"><path d="M0 0L8 7L0 14Z" fill="#7cc8cc"/></svg><a>data quality</a></li>
    <li><svg width="8" height="14"><path d="M0 0L8 7L0 14Z" fill="#7cc8cc"/></svg><a>about us</a></li>
  </ul>
  <div class="side-rule"></div>

  <main class="main">
    <h1>Welcome to Brontaro</h1>
    <p>Brontaro was founded in 1994 by a group of geospatial software engineers that recognised the significant value that data, and the systems used to store and analyse this data, could bring to business.</p>
    <p>Our Customers: We have worked with over 200 companies in a myriad of market sectors - from utilities, local and central government, oil and gas, to many spheres of the marine industry.</p>
    <p>Our Pedigree: We provide a vast bank of knowledge and experience to offer an all encompassing service. This ensures that you, as a customer, reap the maximum benefits from your data and systems through utilising a combination of our skilled consultants, analysts and developers that will work with you and your requirements to help achieve your business objectives.</p>
    <p>Our People: We have a wide ranging skill set including QUADRA 2 qualified Project Managers, fully qualified Software Developers and Experienced Data Consultants.</p>
    <p>We can be on hand to help with any or all parts of your data projects via:</p>
    <ul class="services">
      <li>* <a>Data Consultancy</a></li>
      <li>* <a>System Consultancy</a></li>
      <li>* <a>Software Development</a></li>
    </ul>
  </main>
</div>

<footer>
  <div class="copyright">Copyright Notice © 2009 brontaro-example.co.uk. All rights reserved.</div>
  <div class="social" aria-label="Social network links">
    <span style="width:33px"></span>
    <span style="width:63px;background:#333"></span>
    <span style="width:25px;background:#5ab6e4"></span>
    <span style="width:25px;background:#2a78b4"></span>
    <span style="width:25px;background:#2e5fa8"></span>
  </div>
</footer>
</body>
</html>
```